Velvetorchid Hair & Beauty Business Card

Velvetorchid Hair & Beauty is a boutique salon located in the picturesque Lake Taupo NZ. The salon is very luxurious, opulent gold gilded mirrors, chandelier lit, contemporary french decor, sets the mood to create beautiful hair, makeup and all beauty services. Just had a new logo design and now after a new business card.
Logo
14 Kerewhenua Street
Taupo
Phone (07) 384 6139
www.velvetorchid.co.nz
email hair@velvetorchid.co.nz
Lorinda Feltham
Also need a space to put in Stylist name, date, appointment time. thanks;)
Another idea is we could incorporate the wallpaper in the back ground either on the back or front or use an ornate glided frame (around the edge of the card) like on my website where my brides photos flash.
Decided against the wall paper but at least you can see our colour theme for the salon.
Updates

Please check out my updated brief . Thanks :)

Target Market(s)

25-60 years plus, mainly mid age females , wanting the best possible service , high standard of workmanship and money not a problem.

Industry/Entity Type

Boutique

Requirements
Must have
• Gold and silver

```html
<!DOCTYPE html>
<html lang="en">
<head>
<meta charset="utf-8">
<title>Velvetorchid Hair &amp; Beauty – Business Card</title>
<link rel="stylesheet" href="https://fonts.googleapis.com/css2?family=Comfortaa:wght@400&display=swap">
<style>
  :root {
    --page: #ffffff;
    --card-light: #fbfbfb;
    --card-mid: #f2f1f1;
    --petal-warm: rgba(236, 214, 206, 0.35);
    --petal-cool: rgba(222, 224, 220, 0.45);
    --gold: #8a6c14;
    --ink: #646464;
  }
  html, body {
    margin: 0;
    padding: 0;
    width: 1200px;
    height: 686px;
    overflow: hidden;
    background: var(--page);
  }
  .card {
    position: relative;
    width: 1200px;
    height: 686px;
    background: var(--page);
    font-family: "Comfortaa", sans-serif;
  }
  .card-face {
    position: absolute;
    left: 21px;
    top: 21px;
    width: 1158px;
    height: 642px;
    background:
      radial-gradient(circle at 80% 20%, var(--petal-warm) 0, transparent 32%),
      radial-gradient(circle at 22% 80%, var(--petal-cool) 0, transparent 30%),
      radial-gradient(circle at 55% 45%, var(--petal-warm) 0, transparent 25%),
      linear-gradient(135deg, var(--card-mid), var(--card-light) 45%, var(--card-mid));
  }
  .wallpaper {
    position: absolute;
    inset: 0;
  }
  .brand {
    position: absolute;
    left: 78px;
    top: 196px;
    width: 560px;
    text-align: center;
    color: var(--gold);
    font-weight: 400;
  }
  .brand-name {
    display: block;
    font-size: 76px;
    line-height: 1;
    letter-spacing: -1px;
  }
  .brand-tagline {
    display: block;
    margin-top: 22px;
    font-size: 24px;
    letter-spacing: 3px;
    text-transform: uppercase;
  }
  .contact {
    position: absolute;
    left: 508px;
    top: 348px;
    margin: 0;
    padding: 0;
    list-style: none;
    color: var(--ink);
    font-size: 38px;
    line-height: 56px;
    white-space: nowrap;
  }
</style>
</head>
<body>
  <div class="card">
    <div class="card-face">
      <div class="wallpaper" role="img" aria-label="Faint floral wallpaper pattern in soft blush and grey tones"></div>

      <div class="brand">
        <span class="brand-name">Velvetorchid</span>
        <span class="brand-tagline">Hair &amp; Beauty</span>
      </div>

      <ul class="contact">
        <li class="contact-street">14 Kerewhenua Street</li>
        <li class="contact-town">Taupo</li>
        <li class="contact-phone">Phone (07) 384 6139</li>
        <li class="contact-web">www.velvetorchid.co.nz</li>
        <li class="contact-email">Email hair@velvetorchid.co.nz</li>
      </ul>
    </div>
  </div>
</body>
</html>
```